Logo-Design für Oldtimerhandel Wendtner&Wendtner klassische Automobile OG
Zielgruppe
Handel mit Oldtimern, speziell aus den 60er und 70er Jahren. Zielgruppe sind überwiegend Menschen, die sich von der Masse abheben möchten und Wert auf etwas Einzigartiges legen.
Aufgabenstellung
Das Design soll ein hochwertiges Gesamterscheinungsbild mit gutem Wiedererkennungswert haben. Auch kann ein stilisierter Oldtimer Teil des Logos sein, um für die Zielgruppe besser erkennbar zu sein.
Das Logo muss für Homepage, Visitkarten, Briefpapier etc. tauglich sein und auch in S/W gut erkennbar sein können. Ebenso sollte es möglich sein, Autos mit dem Logo bzw. Schriftzug zu branden.
Beispielhaft wäre das Logo bzw. der Internetauftritt von http://www.moravek-vintage-motors.com vergleichbar.

```html
<!DOCTYPE html>
<html lang="de">
<head>
<meta charset="utf-8">
<title>Wendtner &amp; Wendtner – Geschäftsausstattung</title>
<link rel="stylesheet" href="https://fonts.googleapis.com/css2?family=EB+Garamond:wght@500&family=Mulish:wght@400;500;600&display=swap">
<style>
  :root{
    --backdrop:#2f2f31;
    --brand-blue:#6480a1;
    --lavender:#c5c9da;
    --lavender-pale:#e3e4ec;
    --paper:#ffffff;
    --ink:#232329;
    --grey-text:#8c8c92;
    --rule:#9aa6bd;
  }
  *{margin:0;padding:0;box-sizing:border-box}
  html,body{width:1200px;height:848px;overflow:hidden;background:var(--backdrop)}
  .canvas{position:relative;width:1200px;height:848px;font-family:"Mulish",sans-serif;color:var(--ink)}
  .sheet{position:absolute;width:498px;height:705px}
  .sheet--back{left:53px;top:74px;background:var(--brand-blue)}
  .sheet--letter{left:443px;top:43px;background:var(--paper)}
  .illustration{position:absolute;border-radius:50% 50% 8px 8px / 70% 70% 8px 8px}
  .illustration--back{left:117px;top:525px;width:267px;height:154px;
    background:linear-gradient(180deg,#c7cbdb 0%,#a5b0c8 70%,#1c1c22 100%)}
  .illustration--letter{left:349px;top:22px;width:128px;height:74px;
    background:linear-gradient(180deg,var(--lavender) 0%,var(--brand-blue) 65%,#1c1c22 100%)}
  .company-name{position:absolute;font-family:"Mulish",sans-serif;font-weight:600;color:var(--ink);line-height:1.25;white-space:nowrap}
  .company-name--letter{left:50px;top:60px;font-size:14px}
  .company-name--card-front{left:0;right:0;top:80px;font-size:10px;text-align:center}
  .company-name--card-back{left:12px;top:16px;font-size:7.5px}
  .return-line{position:absolute;left:65px;top:123px;font-size:4px;color:var(--grey-text)}
  .contact{position:absolute;left:390px;top:125px;font-size:5.4px;line-height:8.3px;color:var(--grey-text);font-style:normal}
  .contact p+p{margin-top:5px}
  .fold-mark{position:absolute;left:2px;width:7px;height:1px;background:#c8c8cc}
  .footer{position:absolute;left:0;right:0;top:667px;text-align:center;font-size:5px;line-height:8.5px;color:var(--grey-text)}
  .card{position:absolute;width:201px;height:130px;background:var(--paper);box-shadow:0 2px 6px rgba(0,0,0,.45);overflow:hidden}
  .card--front{left:960px;top:226px}
  .card--back{left:922px;top:370px}
  .illustration--card-front{left:62px;top:20px;width:76px;height:47px;
    background:linear-gradient(180deg,var(--lavender) 0%,var(--brand-blue) 65%,#1c1c22 100%)}
  .card__head{position:absolute;left:0;top:0;width:100%;height:49px;background:var(--paper);border-bottom:1px solid var(--rule)}
  .illustration--card-back{left:136px;top:8px;width:57px;height:34px;
    background:linear-gradient(180deg,var(--lavender) 0%,var(--brand-blue) 65%,#1c1c22 100%)}
  .card__body{position:absolute;left:0;top:50px;width:100%;height:80px;background:var(--lavender-pale);text-align:center}
  .person{margin-top:17px;font-family:"EB Garamond",serif;font-size:11px;color:var(--brand-blue)}
  .role{margin-top:3px;font-size:4.6px;letter-spacing:.14em;color:#55565e}
  .card-contact{margin-top:14px;font-size:4.6px;line-height:7.5px;color:var(--ink)}
</style>
</head>
<body>
<main class="canvas">

  <section class="sheet sheet--back" aria-label="Rückseite Briefpapier">
    <div class="illustration illustration--back" role="img" aria-label="Illustration eines klassischen Automobils der 50er Jahre vor hellem Bogen"></div>
  </section>

  <section class="sheet sheet--letter" aria-label="Briefbogen">
    <p class="company-name company-name--letter">Wendtner &amp; Wendtner<br>klassische Automobile OG</p>
    <div class="illustration illustration--letter" role="img" aria-label="Illustration eines klassischen Automobils"></div>

    <p class="return-line">Wendtner &amp; Wendtner OG, Lindenallee 12, 12345 Beispielstadt</p>

    <address class="contact">
      <p>Wendtner &amp; Wendtner OG<br>Lindenallee 12<br>12345 Beispielstadt</p>
      <p>Fon 0 98 76/54 32 10<br>Fax 0 98 76/54 32 11<br>info@wendtnerwendtner.de<br>www.wendtnerwendtner.de</p>
    </address>

    <span class="fold-mark" style="top:250px"></span>
    <span class="fold-mark" style="top:499px"></span>

    <footer class="footer">
      Handelsregister Amtsgericht Beispielstadt HRA 1234 &nbsp;|&nbsp; Komplementärin: Wendtner &amp; Wendtner OG, Lindenallee 20, 12345 Beispielstadt<br>
      Registergericht: Amtsgericht Beispielstadt HRB 5678 &nbsp;|&nbsp; Geschäftsführerin: Hanna Probstner<br>
      UID: DE 998 877 665 &nbsp;|&nbsp; IBAN DE 00123400000000000000 &nbsp;|&nbsp; BIC BEIS DE X1XXX
    </footer>
  </section>

  <section class="card card--front" aria-label="Visitenkarte Vorderseite">
    <div class="illustration illustration--card-front" role="img" aria-label="Illustration eines klassischen Automobils"></div>
    <p class="company-name company-name--card-front">Wendtner &amp; Wendtner<br>klassische Automobile OG</p>
  </section>

  <section class="card card--back" aria-label="Visitenkarte Rückseite">
    <div class="card__head">
      <p class="company-name company-name--card-back">Wendtner &amp; Wendtner<br>klassische Automobile OG</p>
      <div class="illustration illustration--card-back" role="img" aria-label="Illustration eines klassischen Automobils"></div>
    </div>
    <div class="card__body">
      <p class="person">Konrad Beispielmann</p>
      <p class="role">GESCHÄFTSFÜHRER</p>
      <p class="card-contact">Lindenallee 12 • 12345 Beispielstadt<br>0 98 76/54 32 10 • info@wendtnerwendtner.de • www.wendtnerwendtner.de</p>
    </div>
  </section>

</main>
</body>
</html>
```